Fennick Executive Search - New Business Card Design Project

We are an executive search firm called Fennick Executive Search based in the UK. We require a custom design for a business card. We're looking to convey a professional service to executives for executive search recruitment services. In terms of colours, we like dark blues and grays (maybe even silver incorporated somewhere if we go for a foiled type of card) but we're open to your artistic flare. See our current logo in attachments. We are totally open on design so long as the design is slick and professional.
Updates

Thanks for all your contributions of various designs. I have to say the quality of work has been amazing which is going to make our job quite difficult in the coming days on making a decision. Thanks to you all that have taken the time to submit designs thus far. We'll keep on reviewing and try to narrow down our selection as soon as possible.

Target Market(s)

Executive Search

Industry/Entity Type

Recruitment

Contact Information for Business Card

Fennick Executive Search,
Exclusively Sourcing & Hiring Senior Leaders
Gordon Pellbury, Managing Director,
07823 906417
0117 486 7132
gordon@fennickexecutive.co.uk
fennickexecutive.co.uk
58 Lindmoor Court, Hatherley Road, Bristol, BS32 9QJ

Font styles to use
Sans Serif
Other font styles liked:
• Roboto (which is used in our logo)

Requirements
Must have
• Our logo (It has a subtle fade on it from #02071d at top to #333649 at bottom)
• The logo can be on one side or both sides
• Must be elegant and professional
• We have 2nd slogan CONSULT | INSPIRE | INNOVATE | DELIVER which can be incorporated into the card
Nice to have
• Use of blues and grey colours
• Compatible with similar styling to our website fennickexecutive.co.uk
Should not have
• Must not be overly brash
• Must not contain cartoon characters

```html
<!DOCTYPE html>
<html lang="en">
<head>
<meta charset="utf-8">
<title>Fennick Executive Search – Business Card</title>
<link rel="stylesheet" href="https://fonts.googleapis.com/css2?family=Roboto:wght@400;500;700&display=swap">
<style>
  :root {
    --canvas: #efe3e3;
    --navy-deep: #161a2d;
    --navy: #1b1e32;
    --navy-soft: #202338;
    --band: #282a3b;
    --paper: #ffffff;
    --ink: #1b1e33;
    --on-dark: #e9eaf0;
  }
  * { box-sizing: border-box; margin: 0; padding: 0; }
  html, body { width: 1200px; height: 1200px; overflow: hidden; }
  body {
    background: var(--canvas);
    font-family: "Roboto", Arial, sans-serif;
    color: var(--ink);
    position: relative;
  }
  .card {
    position: absolute;
    width: 840px;
    height: 480px;
    background: var(--paper);
    overflow: hidden;
  }
  .card--front { left: 54px; top: 75px; }
  .card--back { left: 266px; top: 657px; }
  .card__wave { position: absolute; left: 0; top: 0; width: 840px; height: 480px; }

  .holder { position: absolute; left: 53px; top: 40px; color: var(--on-dark); }
  .holder__name { font-size: 24px; font-weight: 400; letter-spacing: 0.2px; }
  .holder__title { font-size: 16px; font-weight: 400; margin-top: 9px; letter-spacing: 0.3px; }

  .tagline {
    position: absolute; left: 566px; top: 44px;
    color: var(--on-dark); font-size: 13px; line-height: 17px; letter-spacing: 0.2px;
  }

  .contact { position: absolute; left: 53px; top: 316px; font-size: 13px; }
  .contact__row { display: flex; height: 30px; align-items: center; }
  .contact__label { width: 70px; font-weight: 400; }
  .contact__value { font-weight: 500; }
  .contact__row--address .contact__label { width: 68px; }

  .brand__name {
    position: absolute;
    font-weight: 500; color: var(--ink);
    text-transform: uppercase; letter-spacing: 0.6px;
  }
  .brand__name--front {
    right: 40px; top: 420px;
    font-size: 15px; line-height: 20px; text-align: right;
  }
  .brand__name--back {
    left: 0; right: 0; top: 222px;
    font-size: 24px; line-height: 30px; text-align: center; letter-spacing: 1.2px;
  }

  .slogan {
    position: absolute; left: 0; right: 0; top: 400px;
    text-align: center; font-size: 13px; font-weight: 500; letter-spacing: 0.2px;
  }
</style>
</head>
<body>

  <section class="card card--front" aria-label="Business card front">
    <svg class="card__wave" viewBox="0 0 840 480" aria-hidden="true">
      <rect width="840" height="300" fill="var(--navy)"/>
      <path d="M0 200 C180 135 360 170 560 225 C680 255 780 262 840 258 L840 300 L0 300 Z" fill="var(--navy-soft)"/>
      <path d="M0 200 C160 180 330 195 520 225 C660 245 770 245 840 245 L840 300 L0 300 Z" fill="var(--band)"/>
      <path d="M0 249 C120 220 260 218 420 245 C560 268 700 290 840 285 L840 480 L0 480 Z" fill="var(--paper)"/>
    </svg>

    <div class="holder">
      <h1 class="holder__name">Gordon Pellbury</h1>
      <p class="holder__title">Managing Director</p>
    </div>

    <p class="tagline">Fennick Executive Search,<br>Exclusively Sourcing &amp; Hiring Senior Leaders</p>

    <div class="contact">
      <p class="contact__row"><span class="contact__label">EMAIL:</span><span class="contact__value">gordon@fennickexecutive.co.uk</span></p>
      <p class="contact__row"><span class="contact__label">MOBILE:</span><span class="contact__value">07823 906417 / 0117 486 7132</span></p>
      <p class="contact__row"><span class="contact__label">WEBSITE</span><span class="contact__value">www.fennickexecutive.co.uk</span></p>
      <p class="contact__row contact__row--address"><span class="contact__label">ADDRESS:</span><span class="contact__value">58 Lindmoor Court, Hatherley Road, Bristol, BS32 9QJ</span></p>
    </div>

    <p class="brand__name brand__name--front">Fennick<br>Executive Search</p>
  </section>

  <section class="card card--back" aria-label="Business card back">
    <svg class="card__wave" viewBox="0 0 840 480" aria-hidden="true">
      <rect width="840" height="130" fill="var(--navy-deep)"/>
      <path d="M0 87 C120 68 230 58 360 62 C520 68 680 88 840 73 L840 130 L0 130 Z" fill="var(--band)"/>
      <path d="M0 119 C100 98 200 90 300 91 C460 93 640 118 840 107 L840 480 L0 480 Z" fill="var(--paper)"/>
    </svg>

    <p class="brand__name brand__name--back">Fennick<br>Executive Search</p>

    <p class="slogan">CONSULT | INSPIRE | INNOVATE | DELIVER</p>
  </section>

</body>
</html>
```